The Brambury Firm

We need a new design for our letterhead and envelopes. We are a personal injury and criminal defense firm so we need something modern and clean, but more on the professional/traditional side. Our new logo has two colors and is attached to the file so we need something that works well with those colors/matches the design. The following information needs to be on the letterhead:
Phone: (555) 314-7265
Fax: (555) 419-6032
Toll-Free: (555) 736-1149
Post Office Box 4273
Harlow Ridge, QN 29458-4273
TQHarmClaimsDesk.example
PalmettoShieldCounsel.example

Target Market(s)

Clients, government agencies, other law firms

Industry/Entity Type

Legal

Font styles to use
Sans Serif
Other font styles liked:
• Arial

Colors

Designer to choose colors to be used in the design.

Requirements
Must have
• Must look professional and clean, modern
Nice to have
• I would like to see a design that works with the logo but does not distract from the content that will be printed on it
Should not have
• Too many colors or crazy designs.

```html
<!DOCTYPE html>
<html lang="en">
<head>
<meta charset="utf-8">
<title>The Brambury Firm — Stationery</title>
<link href="https://fonts.googleapis.com/css2?family=Arimo:wght@400;700&display=swap" rel="stylesheet">
<style>
  :root {
    --backdrop: #1e1b1a;
    --paper: #ffffff;
    --brand-red: #c62a2a;
    --brand-navy: #2e2277;
    --ink: #1a1a1a;
  }
  * { margin: 0; padding: 0; box-sizing: border-box; }
  html, body {
    width: 1200px; height: 1200px; overflow: hidden;
    background: var(--backdrop);
    font-family: "Arimo", Arial, sans-serif;
  }
  .sheet {
    position: absolute;
    background: var(--paper);
    overflow: hidden;
  }
  .envelope { left: 350px; top: 72px; width: 532px; height: 294px; }
  .letterhead { left: 350px; top: 393px; width: 532px; height: 752px; }
  .corner-art {
    position: absolute; inset: 0;
    width: 100%; height: 100%;
  }
  .firm-mark {
    position: absolute;
    display: flex; align-items: center; gap: 6px;
  }
  .firm-mark .dot {
    width: 12px; height: 12px; border-radius: 50%;
    background: var(--brand-red);
  }
  .firm-mark .name {
    font-weight: 700; color: var(--brand-navy);
    font-size: 15px; letter-spacing: 0.2px; white-space: nowrap;
  }
  .envelope .firm-mark { left: 48px; top: 62px; }
  .letterhead .firm-mark { left: 34px; top: 70px; }
  .contact {
    position: absolute;
    text-align: center; color: var(--ink);
    white-space: nowrap;
  }
  .contact .sep {
    display: inline-block; border-left: 1px solid var(--ink);
    height: 1.1em; vertical-align: -0.2em; margin: 0 3px;
  }
  .envelope .contact {
    left: 14px; top: 104px; width: 180px;
    font-size: 5.3px; line-height: 6.5px;
  }
  .letterhead .contact {
    right: 12px; top: 710px; width: 260px;
    font-size: 8px; line-height: 9.4px;
  }
</style>
</head>
<body>

<section class="sheet envelope">
  <svg class="corner-art" viewBox="0 0 532 294">
    <defs>
      <linearGradient id="env-tone" x1="0" y1="0" x2="1" y2="1">
        <stop offset="0" stop-color="#c62a2a"/>
        <stop offset="1" stop-color="#2e2277"/>
      </linearGradient>
    </defs>
    <polygon role="img" aria-label="Angular red and navy corner graphic, top right" points="334,0 532,0 532,114" fill="url(#env-tone)"/>
    <polygon role="img" aria-label="Angular red and navy corner graphic, bottom left" points="0,154 182,294 0,294" fill="url(#env-tone)"/>
  </svg>
  <div class="firm-mark"><span class="dot"></span><span class="name">The Brambury Firm</span></div>
  <div class="contact">
    Phone: (555) 314-7265<span class="sep"></span>Fax: (555) 419-6032<span class="sep"></span>Toll-Free: (555) 736-1149<br>
    Post Office Box 4273 Harlow Ridge, QN 29458-4273<br>
    TQHarmClaimsDesk.example<span class="sep"></span>PalmettoShieldCounsel.example
  </div>
</section>

<section class="sheet letterhead">
  <svg class="corner-art" viewBox="0 0 532 752">
    <defs>
      <linearGradient id="sheet-tone" x1="0" y1="0" x2="1" y2="1">
        <stop offset="0" stop-color="#c62a2a"/>
        <stop offset="1" stop-color="#2e2277"/>
      </linearGradient>
    </defs>
    <polygon role="img" aria-label="Angular red and navy corner graphic, top right" points="284,0 532,0 532,144" fill="url(#sheet-tone)"/>
    <polygon role="img" aria-label="Angular red and navy corner graphic, bottom left" points="0,551 262,752 0,752" fill="url(#sheet-tone)"/>
  </svg>
  <div class="firm-mark"><span class="dot"></span><span class="name">The Brambury Firm</span></div>
  <div class="contact">
    Phone: (555) 314-7265<span class="sep"></span>Fax: (555) 419-6032<span class="sep"></span>Toll-Free: (555) 736-1149<br>
    Post Office Box 4273 Harlow Ridge, QN 29458-4273<br>
    TQHarmClaimsDesk.example<span class="sep"></span>PalmettoShieldCounsel.example
  </div>
</section>

</body>
</html>
```